Business card for medical clinic

I need an upmarket, modern medical/health business card for my clinic

Contact Information for Business Card

name, address, email, qr code

```html
<!DOCTYPE html>
<html lang="en">
<head>
<meta charset="utf-8">
<title>Meridian Care Partners — Business Card</title>
<link href="https://fonts.googleapis.com/css2?family=Montserrat:wght@300;400;700&display=swap" rel="stylesheet">
<style>
  :root {
    --stage: #6f6f6f;
    --paper: #ffffff;
    --navy: #1c2847;
    --navy-deep: #16203b;
    --accent: #1e9ad6;
    --ink: #3a3f4a;
    --title-ink: #1c2d52;
  }
  * { box-sizing: border-box; margin: 0; padding: 0; }
  html, body { width: 1200px; height: 800px; overflow: hidden; }
  body {
    background: var(--stage);
    font-family: "Montserrat", sans-serif;
    position: relative;
  }
  .card {
    position: absolute;
    width: 540px;
    height: 310px;
    border-radius: 18px;
    overflow: hidden;
    box-shadow: 0 3px 0 var(--accent), 0 14px 30px rgba(0,0,0,0.3);
  }
  .card-front { left: 50px; top: 110px; background: var(--paper); }
  .card-back { left: 610px; top: 380px; background: var(--navy); }

  .brand {
    position: absolute;
    display: flex;
    align-items: center;
    gap: 12px;
  }
  .brand-dot {
    width: 30px; height: 30px;
    border-radius: 50%;
    border: 3px solid currentColor;
  }
  .brand-name {
    font-weight: 400;
    font-size: 17px;
    letter-spacing: 2px;
    text-transform: uppercase;
    line-height: 1.3;
  }
  .card-front .brand { right: 60px; top: 46px; color: var(--accent); }

  .divider {
    position: absolute;
    left: 30px; right: 26px; top: 162px;
    height: 1px;
    background: var(--accent);
  }
  .holder { position: absolute; left: 36px; top: 108px; }
  .holder-name {
    font-weight: 700;
    font-size: 24px;
    color: var(--title-ink);
    letter-spacing: 0.5px;
    text-transform: uppercase;
  }
  .holder-role { font-weight: 300; font-size: 15px; color: var(--ink); margin-top: 2px; }

  .contacts {
    position: absolute;
    left: 36px; top: 184px;
    list-style: none;
    display: flex;
    flex-direction: column;
    gap: 8px;
  }
  .contacts li {
    display: flex; align-items: center; gap: 10px;
    font-weight: 300; font-size: 15px; color: var(--ink);
  }
  .contacts svg { width: 14px; height: 14px; flex: none; }

  .address {
    position: absolute;
    right: 30px; top: 182px;
    text-align: right;
    font-weight: 300; font-size: 15px; color: var(--ink);
    line-height: 1.55;
  }

  .back-texture {
    position: absolute; inset: 0;
    background: radial-gradient(circle at 80% 30%, #243256 0%, var(--navy) 55%, var(--navy-deep) 100%);
  }
  .card-back .brand { right: 40px; top: 132px; color: #ffffff; }
</style>
</head>
<body>
  <section class="card card-front" aria-label="Business card front">
    <div class="brand">
      <span class="brand-dot"></span>
      <span class="brand-name">Meridian Care<br>Partners</span>
    </div>

    <div class="holder">
      <h1 class="holder-name">Marcus Ellery</h1>
      <p class="holder-role">President</p>
    </div>

    <div class="divider"></div>

    <ul class="contacts">
      <li>
        <svg viewBox="0 0 14 14"><circle cx="7" cy="7" r="7" fill="#1e9ad6"/><path d="M4.3 3.6c.4-.3.8-.2 1 .2l.6 1.1c.2.4.1.7-.2.9l-.4.3c.4.9 1.2 1.7 2.1 2.1l.3-.4c.2-.3.5-.4.9-.2l1.1.6c.4.2.5.6.2 1-.6.8-1.3 1-2.1.6-1.7-.8-2.9-2-3.7-3.7-.4-.8-.2-1.5.2-2.5z" fill="#fff"/></svg>
        555-310-4827
      </li>
      <li>
        <svg viewBox="0 0 14 14"><circle cx="7" cy="7" r="7" fill="#1e9ad6"/><rect x="3.3" y="4.5" width="7.4" height="5" rx="0.6" fill="#fff"/><path d="M3.5 4.8L7 7.4l3.5-2.6" fill="none" stroke="#1e9ad6" stroke-width="0.8"/></svg>
        marcus@meridiancare.com
      </li>
      <li>
        <svg viewBox="0 0 14 14"><circle cx="7" cy="7" r="7" fill="#1e9ad6"/><circle cx="7" cy="7" r="3.6" fill="none" stroke="#fff" stroke-width="0.9"/><ellipse cx="7" cy="7" rx="1.5" ry="3.6" fill="none" stroke="#fff" stroke-width="0.8"/><path d="M3.4 7h7.2" stroke="#fff" stroke-width="0.8"/></svg>
        www.meridiancare.com
      </li>
    </ul>

    <address class="address" style="font-style:normal">
      1820 Harbor View Drive<br>
      Seacliff CA 90210
    </address>
  </section>

  <section class="card card-back" aria-label="Business card back">
    <div class="back-texture" role="img" aria-label="Embossed repeating brand pattern on navy stock"></div>
    <div class="brand">
      <span class="brand-dot"></span>
      <span class="brand-name">Meridian Care<br>Partners</span>
    </div>
  </section>
</body>
</html>
```